Halvorn spray foam and Environmental

I have business cards but need new ones. The ones I have are very bland. Here is. Y company website http://www.halvornsprayfoam.ca

Also I can send you copies of the current cards
I would also need my current logo on the new design as well.. Also spray foam and Environmental

Industry/Entity Type

Business

Logo Text

Halvorn.

```html
<!DOCTYPE html>
<html lang="en">
<head>
<meta charset="utf-8">
<title>Halvorn Business Cards</title>
<link href="https://fonts.googleapis.com/css2?family=Open+Sans:wght@700;800&family=EB+Garamond:wght@500&display=swap" rel="stylesheet">
<style>
  :root {
    --backdrop: #efe6da;
    --purple: #6a3a8c;
    --green: #3cb43c;
    --green-text: #7cc224;
    --orange: #f07a1e;
    --orange-text: #f39a16;
    --grey: #6f6f6f;
    --foam-light: #fbfbf8;
    --foam-mid: #e9e7e1;
  }
  * { margin: 0; padding: 0; box-sizing: border-box; }
  html, body { width: 1200px; height: 787px; overflow: hidden; }
  body {
    background: var(--backdrop);
    position: relative;
    font-family: "Open Sans", Arial, sans-serif;
  }
  .card {
    position: absolute;
    width: 450px;
    height: 250px;
    border-radius: 16px;
    border: 7px solid var(--green);
    overflow: hidden;
    box-shadow: 0 6px 14px rgba(0,0,0,0.18);
  }
  .card--environmental { left: 225px; top: 140px; border-color: var(--green); color: var(--green-text); }
  .card--sprayfoam { left: 560px; top: 360px; border-color: var(--orange); color: var(--orange-text); }
  .foam-backdrop {
    position: absolute; inset: 0;
    background: radial-gradient(ellipse at 70% 30%, var(--foam-light), var(--foam-mid));
  }
  .el { position: absolute; font-weight: 800; white-space: nowrap; }
  .contact { font-size: 11px; line-height: 1.35; font-weight: 700; }
  .phone { font-size: 17px; }
  .brand { display: flex; align-items: center; gap: 10px; }
  .brand-square { width: 56px; height: 40px; border-radius: 6px; background: var(--grey); }
  .brand-name { font-size: 31px; color: var(--purple); font-weight: 800; letter-spacing: 0.5px; line-height: 1; }
  .division { font-size: 15px; font-weight: 700; letter-spacing: 0.5px; }
  .division--purple { color: var(--purple); font-weight: 800; }
  .tagline { font-family: "EB Garamond", Georgia, serif; font-weight: 500; font-size: 22px; }
  .tagline--grey { color: var(--grey); }
  .services { list-style: none; font-size: 12.5px; line-height: 1.25; }
  .services li::before {
    content: ""; display: inline-block; width: 7px; height: 7px; border-radius: 50%;
    background: var(--purple); margin-right: 5px; vertical-align: 1px;
  }
  .services li:nth-child(2) { margin-left: 10px; }
  .services li:nth-child(3) { margin-left: 20px; }
</style>
</head>
<body>

<section class="card card--environmental">
  <div class="foam-backdrop" role="img" aria-label="Photo of sprayed white insulation foam between wall studs"></div>
  <p class="el contact" style="left:30px; top:36px;">enviro1@halvornmail.ca<br>www.halvornenvironmental.ca</p>
  <p class="el phone" style="left:295px; top:18px;">604-555-0142</p>
  <div class="el brand" style="left:78px; top:78px;">
    <span class="brand-square"></span>
    <span class="brand-name">HALVORN</span>
  </div>
  <p class="el division" style="left:145px; top:112px;">ENVIRONMENTAL</p>
  <p class="el tagline" style="left:100px; top:134px;">Residental &amp; Commercial</p>
  <ul class="el services" style="left:255px; top:163px;">
    <li>BUILDING DEMOLITION</li>
    <li>LEAD TESTING</li>
    <li>MOULD REMOVAL</li>
  </ul>
  <ul class="el services" style="left:40px; top:182px;">
    <li>AIR MONITORING</li>
    <li>ASBESTOS TESTING</li>
    <li>ASBESTOS REMOVAL</li>
  </ul>
</section>

<section class="card card--sprayfoam">
  <div class="foam-backdrop" role="img" aria-label="Photo of sprayed white insulation foam between wall studs"></div>
  <ul class="el services" style="left:22px; top:40px;">
    <li>ROOFING FOAM</li>
    <li>SLABJACKING</li>
    <li>2 POUND / HALF POUND</li>
  </ul>
  <ul class="el services" style="left:240px; top:16px;">
    <li>SOUND PROOFING</li>
    <li>BATT INSULATION</li>
    <li>ATTIC BLOW IN</li>
  </ul>
  <div class="el brand" style="left:85px; top:90px;">
    <span class="brand-square"></span>
    <span class="brand-name">HALVORN</span>
  </div>
  <p class="el division division--purple" style="left:152px; top:123px;">SPRAY FOAM LTD.</p>
  <p class="el tagline tagline--grey" style="left:95px; top:143px;">Residental &amp; Commercial</p>
  <p class="el phone" style="left:295px; top:178px;">604-555-0178</p>
  <p class="el contact" style="left:40px; top:200px;">halvornfoam@halvornmail.ca<br>www.halvornsprayfoam.ca</p>
</section>

</body>
</html>
```